HR Company Website

Home page and information page needs for Human resources company
SERVICES

Employment Law - -
HR Advice -
Recruitment -
Disciplinaries -
Redundancies -
Coaching & Training -
HR Policy Review -
Contract Writing -
Tribunal Claims -
HR Partner -

LAYOUT SKETCH DISCUSSED:
Yes
On the animation the left hand side messgae banner will be constant along with the button , the right hand side will be animated.

COMPETITION
Vantor HR - www.vantorhr-example.com
Kel HR - www.kelhr-example.co.uk
Brisk HR - www.briskhr-example.com

COMPANY LOGO
Client currently has no logo - Solvinex to design

STRAPLINE:
Brisk HR Partner

ACCREDITATIONS / LOGOS:
Masters Diploma in Emloyment Law

WEBSITE THEME:
Human Resources

MAIN BODY OF WEBSITE:
Light

IMAGES THAT BEST REFLECT YOUR COMPANY:
Staff / Office Based Life style images People groups - no face close ups
planning
infrastructure
NOTHING TOO OBVIOUS

PAGES:

Home
About Us
Our Services
- Employment Law Advice
- HR Advice
- Contracts of Employment
- HR Policies
- Disciplinary Procedures
- Redundancy Advice
Contact Us

MESSAGE BANNERS:
1. 12 Years HR Experience - wealth of experience & knowledge
2. Cost Effective Solution - use us when you need us
3. Personal HR Approach - create bespoke tailored made solutions
4. Preventative Measures Protects - don't leave it until is is too late
5. Complete Peace of Mind - Let us be Brisk HR department

Target Market(s)

Male & Femaie - 30-60

SME Business

Industry/Entity Type

Consulting

Number of Pages Required

2 pages

Requirements
Must have
• This design will be built using the wordpress platform, use the wireframe attached for the layout structure - must be visually impactful - clean and proefessional looking
Nice to have
• I have attached the logo - do not amend the colout but you can add effects onto it if you wish to
Should not have
• Loads of text

```html
<!DOCTYPE html>
<html lang="en">
<head>
<meta charset="utf-8">
<title>Tarnwell HR Ltd – Website Pages</title>
<link href="https://fonts.googleapis.com/css2?family=Arimo:ital,wght@0,400;0,700&display=swap" rel="stylesheet">
<style>
:root{
  --brand-green:#1d8a2c;
  --nav-green:#007a00;
  --bright-green:#22ff22;
  --link-yellow:#ffee33;
  --gold:#c9a227;
  --cta-border:#0a6e1a;
  --cta-light:#dff5f2;
  --cta-dark:#0c978a;
  --footer-grey:#c3c3c3;
  --divider:#5533aa;
  --text:#111;
  --more-blue:#2233cc;
}
*{box-sizing:border-box;margin:0;padding:0}
html,body{width:1200px;height:3070px;overflow:hidden}
body{font-family:"Arimo",Arial,sans-serif;color:var(--text);background:#fff}
.page{position:relative;width:1200px}
.site-header{position:relative;background:#fff;overflow:hidden}
.brand{position:absolute;left:8px}
.brand-name{font-weight:700;font-size:58px;color:var(--brand-green);letter-spacing:-1px;line-height:1}
.brand-strap{display:block;font-size:22px;color:var(--gold);margin:6px 0 0 138px;line-height:1}
.header-swoosh{position:absolute;right:0;top:0}
.main-nav{background:var(--nav-green);height:39px;display:flex;align-items:center;padding-left:45px;gap:30px}
.main-nav a{color:var(--link-yellow);text-decoration:none;font-size:20px}
.hero{background:linear-gradient(180deg,#b7c79a 0%,#8eae5c 35%,#6d9a3a 70%,#a6b487 100%)}
.content-band{background:var(--bright-green);position:relative}
.card{position:absolute;background:#fff;border-radius:6px;box-shadow:0 0 3px rgba(0,0,0,.25)}
.pin{position:absolute;left:-6px;top:-34px}
.card-title{color:var(--brand-green);font-weight:700;font-size:21px;position:absolute;left:40px;top:12px}
.card-text{position:absolute;left:26px;right:22px;top:60px;font-size:15.5px;line-height:22px}
.card-more{position:absolute;right:6px;bottom:6px;font-size:15px;color:var(--more-blue);text-decoration:none}
.about-card .card-title{left:134px;top:10px;font-size:26px}
.about-card .card-text{left:26px;right:26px;top:56px;font-size:15.5px;line-height:22px}
.about-card .card-text p{margin-bottom:22px}
.down-arrow{position:absolute;right:22px;bottom:14px}
.testimonial{background:var(--nav-green);color:#fff;font-size:20px;display:flex;align-items:center;justify-content:center}
.cta-band{position:relative;background:#fff;border-left:2px solid var(--nav-green);border-right:2px solid var(--nav-green)}
.cta-box{position:absolute;width:359px;height:332px;border:6px solid var(--cta-border);background:linear-gradient(135deg,var(--cta-light) 0%,#9fdcd4 45%,var(--cta-dark) 100%)}
.cta-icon{position:absolute;left:14px;top:10px;width:110px;height:90px;transform:rotate(-28deg);border:3px solid #1e6e5a;box-shadow:2px 2px 4px rgba(0,0,0,.3)}
.cta-icon.envelope{background:#eef0f8}
.cta-icon.photo{background:linear-gradient(135deg,#e9d9c6,#b59a82);left:30px}
.cta-icon.contact{background:linear-gradient(135deg,#f4f6f8,#9aa7b6);left:18px;top:22px;transform:rotate(40deg)}
.cta-box .cta-heading{position:absolute;left:0;right:0;top:150px;text-align:center;font-size:25px;color:#333}
.cta-box .cta-text{position:absolute;left:20px;right:20px;top:166px;text-align:center;font-size:15.5px;line-height:22px;text-transform:uppercase}
.cta-box .form-text{position:absolute;left:80px;right:20px;top:158px;font-size:15.5px;line-height:22px}
.site-footer{background:var(--footer-grey);text-align:center}
.footer-nav{display:flex;justify-content:center;gap:0;padding-top:18px}
.footer-nav a{color:#111;text-decoration:none;font-size:20px;margin:0 36px}
.copyright{font-size:15.5px;margin-top:14px}
.page-divider{height:8px;background:var(--divider)}
</style>
</head>
<body>

<!-- Home page -->
<section class="page page-home">
  <header class="site-header" style="height:169px">
    <div class="brand" style="top:52px">
      <span class="brand-name">Tarnwell HR Ltd</span>
      <span class="brand-strap">Brisk HR Partner</span>
    </div>
    <svg class="header-swoosh" width="260" height="169" viewBox="0 0 260 169" aria-hidden="true">
      <defs><linearGradient id="swooshA" x1="0" y1="0" x2="1" y2="1"><stop offset="0" stop-color="#ffffff"/><stop offset="1" stop-color="#0a8a1a"/></linearGradient></defs>
      <path d="M0 169 C120 150 215 110 260 40 L260 169 Z" fill="url(#swooshA)"/>
    </svg>
  </header>
  <nav class="main-nav"><a href="#">Home</a><a href="#">About Us</a><a href="#">Our Services</a><a href="#">Contact Us</a></nav>
  <div class="hero" style="height:419px" role="img" aria-label="Lifestyle photo: a group of friends having a picnic on the grass"></div>

  <main class="content-band" style="height:399px">
    <article class="card" style="left:34px;top:19px;width:350px;height:360px">
      <svg class="pin" width="50" height="60" viewBox="0 0 50 60" aria-hidden="true"><line x1="14" y1="56" x2="24" y2="30" stroke="#888" stroke-width="3"/><circle cx="30" cy="18" r="14" fill="#e01818"/><circle cx="26" cy="14" r="4" fill="#ff8a8a"/></svg>
      <h2 class="card-title">Employment Law Advice</h2>
      <p class="card-text">Lorem ipsum dolor sit amet, consectetur adipiscing elit. Donec nisl magna, congue d ullamcorper quis, faucibus ac diam. Mauris dictum orci vitae neque varius condimentum. Morbi venenatis fringilla risus sed iaculis.Integer luctus orci ac mauris pulvinar idlacinia lorem tincidunt. Suspendisse potenti.Vivamus nec neque sapien.</p>
      <a class="card-more" href="#">More&gt;</a>
    </article>
    <article class="card" style="left:432px;top:19px;width:350px;height:360px">
      <svg class="pin" width="50" height="60" viewBox="0 0 50 60" aria-hidden="true"><line x1="14" y1="56" x2="24" y2="30" stroke="#888" stroke-width="3"/><circle cx="30" cy="18" r="14" fill="#e01818"/><circle cx="26" cy="14" r="4" fill="#ff8a8a"/></svg>
      <h2 class="card-title">Personal HR Approach</h2>
      <p class="card-text">Lorem ipsum dolor sit amet, consectetur adipiscing elit. Donec nisl magna, congue d ullamcorper quis, faucibus ac diam. Mauris dictum orci vitae neque varius condimentum. Morbi venenatis fringilla risus sed iaculis.Integer luctus orci ac mauris pulvinar idlacinia lorem tincidunt. Suspendisse potenti.Vivamus nec neque sapien.</p>
      <a class="card-more" href="#">More&gt;</a>
    </article>
    <article class="card" style="left:824px;top:19px;width:350px;height:360px">
      <svg class="pin" width="50" height="60" viewBox="0 0 50 60" aria-hidden="true"><line x1="14" y1="56" x2="24" y2="30" stroke="#888" stroke-width="3"/><circle cx="30" cy="18" r="14" fill="#e01818"/><circle cx="26" cy="14" r="4" fill="#ff8a8a"/></svg>
      <h2 class="card-title">Rates &amp; Packages</h2>
      <p class="card-text">Lorem ipsum dolor sit amet, consectetur adipiscing elit. Donec nisl magna, congue d ullamcorper quis, faucibus ac diam. Mauris dictum orci vitae neque varius condimentum. Morbi venenatis fringilla risus sed iaculis.Integer luctus orci ac mauris pulvinar idlacinia lorem tincidunt. Suspendisse potenti.Vivamus nec neque sapien.</p>
      <a class="card-more" href="#">More&gt;</a>
    </article>
  </main>

  <div class="testimonial" style="height:55px">“testimonial goes here - a very pleased client -testimonial goes here - a very pleased client - ”</div>

  <section class="cta-band" style="height:372px">
    <div class="cta-box" style="left:26px;top:19px">
      <div class="cta-icon envelope" role="img" aria-label="Envelope illustration"></div>
      <p class="cta-heading">Contact Details</p>
    </div>
    <div class="cta-box" style="left:416px;top:19px">
      <div class="cta-icon photo" role="img" aria-label="Photo of a customer adviser with a headset"></div>
      <p class="cta-text">Call to action<br>"Is your company breaking the law?<br>Call us today<br>and let us protect your business"</p>
    </div>
    <div class="cta-box" style="left:808px;top:19px">
      <div class="cta-icon contact" role="img" aria-label="Contact card illustration"></div>
      <p class="form-text">CONTACT FORM<br>"Find out now if your business protected"<br>Name<br>Email<br>Telephone<br>Comments</p>
    </div>
  </section>

  <footer class="site-footer" style="height:109px">
    <nav class="footer-nav"><a href="#">Home</a><a href="#">About Us</a><a href="#">Our Services</a><a href="#">Contact Us</a></nav>
    <p class="copyright">Copyright (C) Notice</p>
  </footer>
</section>

<div class="page-divider"></div>

<!-- About page -->
<section class="page page-about">
  <header class="site-header" style="height:146px">
    <div class="brand" style="top:30px">
      <span class="brand-name">Tarnwell HR Ltd</span>
      <span class="brand-strap">Brisk HR Partner</span>
    </div>
    <svg class="header-swoosh" width="260" height="146" viewBox="0 0 260 146" aria-hidden="true">
      <defs><linearGradient id="swooshB" x1="0" y1="0" x2="1" y2="1"><stop offset="0" stop-color="#ffffff"/><stop offset="1" stop-color="#0a8a1a"/></linearGradient></defs>
      <path d="M0 146 C120 130 215 95 260 20 L260 146 Z" fill="url(#swooshB)"/>
    </svg>
  </header>
  <nav class="main-nav"><a href="#">Home</a><a href="#">About Us</a><a href="#">Our Services</a><a href="#">Contact Us</a></nav>
  <div class="hero" style="height:420px" role="img" aria-label="Lifestyle photo: a group of friends having a picnic on the grass"></div>

  <main class="content-band" style="height:395px">
    <article class="card about-card" style="left:34px;top:19px;width:1133px;height:356px">
      <svg class="pin" width="50" height="60" viewBox="0 0 50 60" aria-hidden="true"><line x1="14" y1="56" x2="24" y2="30" stroke="#888" stroke-width="3"/><circle cx="30" cy="18" r="14" fill="#e01818"/><circle cx="26" cy="14" r="4" fill="#ff8a8a"/></svg>
      <h1 class="card-title">About Us</h1>
      <div class="card-text">
        <p>Lorem ipsum dolor sit amet, consectetur adipiscing elit. Donec nisl magna, congue d ullamcorper quis, faucibus ac diam. Mauris dictum orci vitae neque varius condimentum.Morbi venenatis fringilla risus sed iaculis.Integer luctus orci ac mauris pulvinar idlacinia lorem tincidunt. Suspendisse potenti.Vivamus nec neque sapien.</p>
        <p>Lorem ipsum dolor sit amet, consectetur adipiscing elit. Donec nisl magna, congue d ullamcorper quis, faucibus ac diam. Mauris dictum orci vitae neque varius condimentum.Morbi venenatis fringilla risus sed iaculis.Integer luctus orci ac mauris pulvinar idlacinia lorem tincidunt. Suspendisse potenti.Vivamus nec neque sapien.</p>
        <p>Lorem ipsum dolor sit amet, consectetur adipiscing elit. Donec nisl magna, congue d ullamcorper quis, faucibus ac diam. Mauris dictum orci vitae neque varius condimentum.Morbi venenatis fringilla risus sed iaculis.Integer luctus orci ac mauris pulvinar idlacinia lorem tincidunt. Suspendisse potenti.Vivamus nec neque sapien.</p>
      </div>
      <svg class="down-arrow" width="36" height="36" viewBox="0 0 36 36" aria-hidden="true"><path d="M11 2 H25 V16 H34 L18 34 L2 16 H11 Z" fill="#3cc23c" stroke="#1d8a2c" stroke-width="1.5"/></svg>
    </article>
  </main>

  <div class="testimonial" style="height:57px">“testimonial goes here - a very pleased client -testimonial goes here - a very pleased client - ”</div>

  <section class="cta-band" style="height:369px">
    <div class="cta-box" style="left:26px;top:18px">
      <div class="cta-icon envelope" role="img" aria-label="Envelope illustration"></div>
      <p class="cta-heading">Contact Details</p>
    </div>
    <div class="cta-box" style="left:416px;top:18px">
      <div class="cta-icon photo" role="img" aria-label="Photo of a customer adviser with a headset"></div>
      <p class="cta-text">Call to action<br>"Is your company breaking the law?<br>Call us today<br>and let us protect your business"</p>
    </div>
    <div class="cta-box" style="left:808px;top:18px">
      <div class="cta-icon contact" role="img" aria-label="Contact card illustration"></div>
      <p class="form-text">CONTACT FORM<br>"Find out now if your business protected"<br>Name<br>Email<br>Telephone<br>Comments</p>
    </div>
  </section>

  <footer class="site-footer" style="height:74px">
    <nav class="footer-nav"><a href="#">Home</a><a href="#">About Us</a><a href="#">Our Services</a><a href="#">Contact Us</a></nav>
    <p class="copyright" style="margin-top:8px">Copyright (C) Notice</p>
  </footer>
</section>

</body>
</html>
```